Modern Business Card

Modern professional business card with more than just logo and demographic info. Something memorable.

We are a trendy/modern chiropractic group with an emphasis on neurology, hence the minimalist-type brain logo. We want to convey that modern and technical aspect with professionalism and the elite nature of our practice environment.

```html
<!DOCTYPE html>
<html lang="en">
<head>
<meta charset="utf-8">
<title>Verity Chiropractic – Business Card</title>
<link href="https://fonts.googleapis.com/css2?family=Cinzel:wght@400;700&family=Open+Sans:wght@400;600&display=swap" rel="stylesheet">
<style>
  :root {
    --brand-blue: #4780c2;
    --brand-blue-soft: #5a8fcc;
    --ink: #2b2b2b;
    --muted: #4a4a4a;
    --paper: #ffffff;
    --backdrop: #e9eaec;
  }
  * { box-sizing: border-box; margin: 0; padding: 0; }
  html, body { width: 1200px; height: 900px; overflow: hidden; }
  body {
    background: var(--backdrop);
    font-family: "Open Sans", Arial, sans-serif;
    position: relative;
  }
  .card {
    position: absolute;
    left: 250px;
    width: 700px;
    height: 400px;
    box-shadow: 0 6px 18px rgba(0,0,0,0.12);
    overflow: hidden;
  }

  /* Front */
  .card-front {
    top: 35px;
    background: var(--brand-blue);
  }
  .front-pattern {
    position: absolute;
    left: 200px;
    top: 70px;
    width: 330px;
    height: 270px;
    border-radius: 40px;
    background: radial-gradient(ellipse at center, var(--brand-blue-soft) 0%, rgba(90,143,204,0.55) 55%, rgba(71,128,194,0) 100%);
  }
  .brand-lockup {
    position: absolute;
    left: 0; right: 0; top: 0; bottom: 0;
    display: flex;
    align-items: center;
    justify-content: center;
    gap: 22px;
  }
  .brand-square {
    width: 70px;
    height: 70px;
    flex: none;
  }
  .card-front .brand-square { background: var(--paper); }

  .wordmark {
    font-family: "Cinzel", Georgia, serif;
    font-weight: 400;
    line-height: 1;
    text-align: left;
  }
  .wordmark-line-main { display: block; }
  .wordmark-line-sub { display: block; }
  .card-front .wordmark { color: var(--paper); }
  .card-front .wordmark-line-main { font-size: 70px; letter-spacing: 2px; }
  .card-front .wordmark-line-sub { font-size: 34px; letter-spacing: 3px; margin-top: 2px; }

  /* Back */
  .card-back {
    top: 465px;
    background: var(--paper);
  }
  .card-back .brand-lockup {
    left: auto; right: 44px; top: 48px; bottom: auto;
    gap: 12px;
  }
  .card-back .brand-square {
    width: 38px;
    height: 38px;
    background: var(--brand-blue);
  }
  .card-back .wordmark { color: var(--ink); }
  .card-back .wordmark-line-main { font-size: 36px; letter-spacing: 1px; }
  .card-back .wordmark-line-sub { font-size: 17px; letter-spacing: 2px; }

  .bottom-band {
    position: absolute;
    left: 0; right: 0; bottom: 0;
    height: 16px;
    background: var(--brand-blue);
  }
  .identity {
    position: absolute;
    left: 0;
    top: 118px;
    padding-left: 50px;
  }
  .identity-bar {
    position: absolute;
    left: 0; top: 8px;
    width: 26px; height: 56px;
    background: var(--brand-blue);
  }
  .person-name {
    font-family: "Cinzel", Georgia, serif;
    font-weight: 700;
    font-size: 30px;
    line-height: 1.2;
    color: var(--brand-blue);
    letter-spacing: 0.5px;
  }
  .person-role {
    font-size: 17px;
    color: var(--muted);
    margin-top: 2px;
  }
  .address {
    position: absolute;
    left: 76px;
    top: 215px;
    font-size: 17px;
    line-height: 1.35;
    color: var(--muted);
  }
  .contacts {
    position: absolute;
    left: 76px;
    top: 282px;
    list-style: none;
    font-size: 17px;
    line-height: 1.35;
    color: var(--muted);
  }
  .contacts li { display: flex; align-items: center; gap: 8px; }
  .contacts svg { width: 13px; height: 13px; fill: var(--brand-blue); flex: none; }
</style>
</head>
<body>
  <section class="card card-front" aria-label="Card front">
    <div class="front-pattern" role="img" aria-label="Faint decorative stripe pattern behind the practice name"></div>
    <div class="brand-lockup">
      <span class="brand-square" aria-hidden="true"></span>
      <div class="wordmark">
        <span class="wordmark-line-main">VERITY</span>
        <span class="wordmark-line-sub">CHIROPRACTIC</span>
      </div>
    </div>
  </section>

  <section class="card card-back" aria-label="Card back">
    <div class="brand-lockup">
      <span class="brand-square" aria-hidden="true"></span>
      <div class="wordmark">
        <span class="wordmark-line-main">VERITY</span>
        <span class="wordmark-line-sub">CHIROPRACTIC</span>
      </div>
    </div>

    <div class="identity">
      <span class="identity-bar"></span>
      <h1 class="person-name">DANIEL MARSH</h1>
      <p class="person-role">Senior Partner</p>
    </div>

    <p class="address">12 Fennel Road Northcliff,<br>Johannesburg, 2195</p>

    <ul class="contacts">
      <li>
        <svg viewBox="0 0 16 16" aria-hidden="true"><path d="M3.5 1l2.5 3-1.5 1.6c.8 2 2.4 3.6 4.4 4.4L10.5 8.5l3 2.5-1.5 3C6.5 14 2 9.5 2 3z"/></svg>
        +120 5555 0148
      </li>
      <li>
        <svg viewBox="0 0 16 16" aria-hidden="true"><path d="M4 0h8a1 1 0 011 1v14a1 1 0 01-1 1H4a1 1 0 01-1-1V1a1 1 0 011-1zm1 2v10h6V2zm3 11a1 1 0 100 2 1 1 0 000-2z"/></svg>
        +965 5550 2716
      </li>
      <li>
        <svg viewBox="0 0 16 16" aria-hidden="true"><path d="M1 3h14v10H1zm1.5 1.2V5l5.5 4 5.5-4v-.8z"/></svg>
        info@veritychiropractic.com
      </li>
      <li>
        <svg viewBox="0 0 16 16" aria-hidden="true"><circle cx="8" cy="8" r="7"/></svg>
        www.veritychiropractic.com
      </li>
    </ul>

    <div class="bottom-band"></div>
  </section>
</body>
</html>
```